Etiketten-Design für österreichischen Qualitätswein gesucht
Zielgruppe
Der Name unseres Weingutes ist HARLO. Wir produzieren österreichische Qualitätsweine und vermarkten diese unter dem Namen HARLO.
Die Weine werden über den Lebensmitteleinzelhandel vertrieben und sollen ein urbanes Publikum zum Impulskauf ansprechen. Es sollte eine grafische Darstellung von einem Fuchs vorkommen. Es kann natürlich Stockmaterial verwendet werden. Das Etikett kann seriös, lustig oder frech sein. Es kann zum Beispiel eine bekannte Fabel mit einem Fuchs darstellen.
Aufgabenstellung
Maximale Höhe: 10,5cm
Papierfarbe: weiß
Folgende Angaben sind am Etikett erforderlich:
- Name: HARLO
- Weinsorte: SAUVIGNON BLANC
- Herkunft: BURGENLAND - ÖSTERREICH

```html
<!DOCTYPE html>
<html lang="de">
<head>
<meta charset="utf-8">
<title>Weingut HARLO – Sauvignon Blanc Etikett</title>
<link rel="stylesheet" href="https://fonts.googleapis.com/css2?family=Bebas+Neue&family=Fira+Sans+Condensed:wght@300;400;500&display=swap">
<style>
  :root {
    --page-bg: #f7f7f7;
    --label-paper: #eef1f0;
    --ink: #111010;
    --accent-red: #e0483c;
    --art-tone-light: #e4e7e6;
    --art-tone-dark: #cfd3d2;
  }
  * { margin: 0; padding: 0; box-sizing: border-box; }
  html, body {
    width: 1200px;
    height: 1200px;
    overflow: hidden;
    background: var(--page-bg);
  }
  .wine-label {
    position: absolute;
    left: 178px;
    top: 80px;
    width: 845px;
    height: 1040px;
    background: var(--label-paper);
    font-family: "Fira Sans Condensed", "Arial Narrow", sans-serif;
    color: var(--ink);
  }
  .stripe {
    position: absolute;
    left: 0;
    width: 100%;
    height: 6px;
    background: var(--accent-red);
  }
  .stripe--top-1 { top: 2px; }
  .stripe--top-2 { top: 16px; }
  .stripe--bottom { bottom: 2px; }
  .label-artwork {
    position: absolute;
    left: 422px;
    top: 88px;
    width: 390px;
    height: 466px;
    background: radial-gradient(ellipse at 60% 55%, var(--art-tone-dark), var(--art-tone-light) 70%, var(--label-paper));
  }
  .winery-prefix {
    position: absolute;
    left: 71px;
    top: 506px;
    font-size: 42px;
    font-weight: 400;
    letter-spacing: 1px;
    line-height: 1;
  }
  .name-bar {
    position: absolute;
    left: 71px;
    top: 556px;
    width: 744px;
    height: 22px;
    background: var(--ink);
  }
  .winery-name {
    position: absolute;
    left: 0;
    width: 858px;
    top: 590px;
    text-align: center;
    font-family: "Bebas Neue", "Oswald", sans-serif;
    font-size: 262px;
    line-height: 0.8;
    letter-spacing: 2px;
  }
  .wine-variety {
    position: absolute;
    left: 0;
    width: 886px;
    top: 822px;
    text-align: center;
    font-size: 36px;
    font-weight: 300;
    letter-spacing: 0.5px;
  }
  .wine-origin {
    position: absolute;
    left: 0;
    width: 908px;
    top: 884px;
    text-align: center;
    font-size: 27px;
    font-weight: 500;
    letter-spacing: 1.5px;
  }
</style>
</head>
<body>
  <main class="wine-label">
    <div class="stripe stripe--top-1"></div>
    <div class="stripe stripe--top-2"></div>

    <div class="label-artwork" role="img" aria-label="Linienzeichnung eines sitzenden Tieres, das auf dem Namensbalken ruht"></div>

    <p class="winery-prefix">WEINGUT</p>
    <div class="name-bar"></div>
    <h1 class="winery-name">HARLO</h1>

    <p class="wine-variety">2019 SAUVIGNON BLANC</p>
    <p class="wine-origin">BURGENLAND-ÖSTERREICH</p>

    <div class="stripe stripe--bottom"></div>
  </main>
</body>
</html>
```